Wix web design for healthcare IT consulting firm.

I am looking for a web design built in Wix that it will be easy for me to add or edit content in the future. The web site does not need to be overly complicated, but it should look very polished and professional. I also want to ensure it is mobile device friendly. I do not need any type of on-line purchasing ability. I will eventually do blogs, but for now it is a fairly standard web site with main page, about us, services provided, etc. I would also like a place for potential customers to contact us directly from the web site. I have included a Word document with some content for the web design. I have also included my logo and business card for reference. I would like to utilize similar colors as my business card. One of my primary competitors is https://vonmarlhq.example/

Target Market(s)

Target market could be nursing home CEO, CIO, or other leader at an organization that manages long term care facilities.

Number of Pages Required

5+ page

Colors
876aae

Requirements
Must have
• Be designed to be used in Wix. Use the content I provided to create and make web design. Allow to be viewed on mobile device. Please use similar color structure as attached business card. Please use attached logo in design.

```html
<!DOCTYPE html>
<html lang="en">
<head>
<meta charset="utf-8">
<title>VitaLink Health Solutions</title>
<link href="https://fonts.googleapis.com/css2?family=Raleway:wght@400;600;700&family=Montserrat:wght@400;500;600&display=swap" rel="stylesheet">
<style>
:root{
  --purple:#6c4a9f;
  --purple-dark:#5d3f8c;
  --field:#5a3b88;
  --ink:#2b2b2b;
  --muted:#6b6b6b;
  --panel:#f1f1f1;
  --footer:#333333;
  --white:#ffffff;
}
*{margin:0;padding:0;box-sizing:border-box}
html,body{width:1200px;height:3557px;overflow:hidden}
body{font-family:"Montserrat",sans-serif;color:var(--ink);background:var(--white);position:relative}
section,header,footer{position:absolute;left:0;width:1200px}
.abs{position:absolute}
.heading{font-family:"Raleway",sans-serif;font-weight:700;font-size:36px;text-align:center;width:1200px;left:0}

/* hero */
.hero{top:0;height:647px;background:linear-gradient(135deg,#5b5a5e 0%,#3d3c40 45%,#2b2a2e 100%)}
.hero-tile{position:absolute;background:rgba(255,255,255,.12)}
.hero-tile.violet{background:rgba(108,74,159,.55)}
.brand{left:78px;top:30px;color:var(--white);font-family:"Raleway",sans-serif;font-weight:700;font-size:40px;display:flex;align-items:center;gap:12px}
.brand .mark{width:26px;height:26px;border:3px solid var(--white)}
.nav{right:80px;top:44px;display:flex;gap:42px;font-size:15px;color:var(--white);letter-spacing:.5px}
.nav a{color:inherit;text-decoration:none;padding-bottom:12px}
.nav a.active{border-bottom:3px solid var(--purple)}
.hero h1{top:272px;width:1200px;text-align:center;color:var(--white);font-family:"Raleway",sans-serif;font-weight:700;font-size:39px;line-height:54px}
.hero p{top:392px;width:1200px;text-align:center;color:var(--white);font-size:22px}

/* welcome */
.welcome{top:647px;height:458px}
.welcome .heading{top:48px;color:var(--purple)}
.device{left:78px;top:135px;width:492px;height:270px;border-radius:14px;background:linear-gradient(160deg,#3c4660,#8aa0c0 50%,#5d6675)}
.mission{left:676px;top:125px;width:420px}
.mission h3{font-family:"Raleway",sans-serif;font-weight:500;font-size:25px;color:var(--ink);margin-bottom:14px}
.mission p{font-size:14px;color:var(--muted);line-height:26px;margin-bottom:10px}
.mission h3+p{margin-bottom:28px}

/* values */
.values{top:1105px;height:669px;background:var(--purple);color:var(--white)}
.values .heading{top:48px}
.value{width:300px;text-align:center}
.value svg{display:block;margin:0 auto 22px}
.value span{font-size:19px}
.rule{position:absolute;background:rgba(255,255,255,.55)}

/* services */
.services{top:1774px;height:602px;background:linear-gradient(180deg,#3a3a3e,#2c2c30 60%,#3b3d44)}
.services .heading{top:44px;color:var(--white)}
.services .intro{left:160px;top:106px;width:880px;color:var(--white);font-size:13.5px;line-height:26px;text-align:center}
.card{top:265px;height:249px;width:498px;border:2px solid rgba(255,255,255,.35);background:rgba(255,255,255,.12);color:var(--white);text-align:center;padding:0 18px}
.card h3{font-family:"Raleway",sans-serif;font-weight:700;font-size:23px;margin-bottom:14px}
.card p{font-size:13.5px;line-height:26px}

/* team */
.team{top:2376px;height:595px}
.team .heading{top:48px;color:var(--purple)}
.portrait{left:78px;top:116px;width:522px;height:356px;background:linear-gradient(90deg,#c9b79a,#e9e2d4 40%,#b7c6cf 70%,#d8cbb4)}
.bio{left:600px;top:116px;width:521px;height:356px;background:var(--panel);padding:72px 54px 0 58px}
.bio h3{font-family:"Raleway",sans-serif;font-weight:500;font-size:25px}
.bio h3 small{font-size:15px;color:var(--muted);font-weight:400}
.bio .role{font-style:italic;font-size:17px;color:var(--muted);margin:14px 0 16px}
.bio p{font-size:13px;line-height:26px;color:var(--muted)}
.bio a{color:var(--ink);font-weight:600;text-decoration:underline}

/* contact */
.contact{top:2971px;height:522px;background:var(--purple);color:var(--white)}
.contact .heading{top:40px}
.channel{width:300px;text-align:center;font-size:14px;line-height:24px}
.field{background:var(--field);color:var(--white);font-size:14px;padding:0 18px;display:flex;align-items:center}
.field.message{align-items:flex-start;padding-top:12px}
.submit{background:var(--white);color:var(--purple);font-weight:700;font-size:19px;letter-spacing:1px;display:flex;align-items:center;justify-content:center}

footer{top:3493px;height:64px;background:var(--footer);color:var(--white);font-size:14px;display:flex;align-items:center;justify-content:center}
</style>
</head>
<body>

<header class="hero" role="img" aria-label="Photo of a healthcare team meeting around a table">
  <div class="hero-tile" style="left:0;top:218px;width:110px;height:175px"></div>
  <div class="hero-tile violet" style="left:0;top:300px;width:110px;height:95px"></div>
  <div class="hero-tile" style="left:960px;top:360px;width:240px;height:160px"></div>
  <div class="hero-tile violet" style="left:960px;top:520px;width:115px;height:127px"></div>
  <div class="hero-tile" style="left:1075px;top:420px;width:125px;height:100px"></div>
  <div class="abs brand"><span class="mark"></span>VitaLink</div>
  <nav class="abs nav"><a class="active" href="#">HOME</a><a href="#">ABOUT</a><a href="#">SERVICES</a><a href="#">BLOG</a><a href="#">CONTACT US</a></nav>
  <h1 class="abs">INCREASING THE VALUE AND SECURITY OF<br>YOUR TECHNOLOGY RESOURCES</h1>
  <p class="abs">Partner with customers to increase the value of their technology tools</p>
</header>

<section class="welcome">
  <h2 class="abs heading">WELCOME TO VitaLink</h2>
  <div class="abs device" role="img" aria-label="Tablet on a keyboard stand showing a clinician at work"></div>
  <div class="abs mission">
    <h3>VitaLink Mission Statement</h3>
    <p>Partner with customers to increase the value of their technology tools</p>
    <h3>VitaLink Niche</h3>
    <p>Understand and get to know customer and their needs</p>
    <p>Committed to be a partner, not vendor</p>
    <p>Provide simplified change management expertise</p>
  </div>
</section>

<section class="values">
  <h2 class="abs heading">OUR CORE VALUES</h2>
  <div class="rule" style="left:25px;top:117px;width:115px;height:2px"></div>
  <div class="rule" style="left:65px;top:117px;width:2px;height:50px"></div>
  <div class="rule" style="left:1070px;top:117px;width:105px;height:2px"></div>
  <div class="rule" style="left:1135px;top:117px;width:2px;height:50px"></div>
  <div class="rule" style="left:365px;top:333px;width:110px;height:2px"></div>
  <div class="rule" style="left:420px;top:285px;width:2px;height:50px"></div>
  <div class="rule" style="left:725px;top:333px;width:110px;height:2px"></div>
  <div class="rule" style="left:780px;top:285px;width:2px;height:50px"></div>
  <div class="rule" style="left:170px;top:586px;width:110px;height:2px"></div>
  <div class="rule" style="left:225px;top:538px;width:2px;height:50px"></div>
  <div class="rule" style="left:545px;top:586px;width:110px;height:2px"></div>
  <div class="rule" style="left:600px;top:538px;width:2px;height:50px"></div>
  <div class="rule" style="left:910px;top:586px;width:110px;height:2px"></div>
  <div class="rule" style="left:965px;top:538px;width:2px;height:50px"></div>

  <div class="abs value" style="left:90px;top:160px">
    <svg width="62" height="62" viewBox="0 0 62 62" fill="none" stroke="#fff" stroke-width="2"><circle cx="31" cy="31" r="28"/><circle cx="31" cy="26" r="7"/><path d="M19 44c3-7 21-7 24 0"/><path d="M31 10v5M14 20l4 3M48 20l-4 3"/></svg>
    <span>Customer Focused</span>
  </div>
  <div class="abs value" style="left:450px;top:160px">
    <svg width="62" height="62" viewBox="0 0 62 62" fill="none" stroke="#fff" stroke-width="2"><rect x="12" y="8" width="34" height="46" rx="2"/><path d="M19 20h20M19 28h14M19 36h10"/><circle cx="44" cy="42" r="9"/><path d="M40 42l3 3 5-6"/></svg>
    <span>Integrity &amp; Ethics</span>
  </div>
  <div class="abs value" style="left:810px;top:160px">
    <svg width="62" height="62" viewBox="0 0 62 62" fill="none" stroke="#fff" stroke-width="2"><rect x="12" y="12" width="38" height="26" rx="2"/><path d="M18 20h26M18 26h26M18 32h26M31 38v10M20 52h22"/></svg>
    <span>Practice Accountability</span>
  </div>
  <div class="abs value" style="left:267px;top:398px">
    <svg width="62" height="62" viewBox="0 0 62 62" fill="none" stroke="#fff" stroke-width="2"><rect x="24" y="8" width="30" height="22" rx="2"/><circle cx="16" cy="20" r="6"/><path d="M8 54V34c0-4 16-4 16 0v20M24 34l8-6"/><path d="M36 30v24"/></svg>
    <span>Professional Development</span>
  </div>
  <div class="abs value" style="left:628px;top:398px">
    <svg width="62" height="62" viewBox="0 0 62 62" fill="none" stroke="#fff" stroke-width="2"><circle cx="31" cy="31" r="27"/><circle cx="31" cy="31" r="20"/><circle cx="24" cy="27" r="1.5" fill="#fff"/><circle cx="38" cy="27" r="1.5" fill="#fff"/><path d="M22 35c4 6 14 6 18 0"/></svg>
    <span>Have Fun</span>
  </div>
</section>

<section class="services" role="img" aria-label="Photo of clinicians at a hospital workstation, darkened">
  <h2 class="abs heading">SERVICES WE PROVIDE</h2>
  <p class="abs intro">We understand different organizations have different needs. VitaLink HS strives to assist your organization by bringing solutions that are easy to understand and allow the customer to track success. We provide solutions based on the customer's needs and desires.<br><br>Typically, all services provided by VitaLink HS will also include a defined deliverable. The purpose is the ensure the value we provide to our customers can be clearly identified and defined prior to the work getting started.</p>
  <div class="abs card" style="left:78px;padding-top:76px">
    <h3>Electronic Health Record (EHR) Services</h3>
    <p>EHR Optimization Services, EHR Implementation, EHR Assessment, EHR Quality Assessment , On-Going EHR Support</p>
  </div>
  <div class="abs card" style="left:623px;padding-top:60px">
    <h3>Information Technology Services</h3>
    <p>Risk Assessment, Policy Management and Consulting , Chief Information Officer (CIO) Services, Chief Information Security Officer (CISO) Services, IT Department Evaluation , On-Going CIO or CISO Support</p>
  </div>
</section>

<section class="team">
  <h2 class="abs heading">LEADERSHIP TEAM</h2>
  <svg class="abs" style="left:40px;top:282px" width="14" height="24" viewBox="0 0 14 24" fill="none" stroke="#6c4a9f" stroke-width="2.5"><path d="M12 2L2 12l10 10"/></svg>
  <div class="abs portrait" role="img" aria-label="Portrait of the company president in scrubs in a hospital corridor"></div>
  <div class="abs bio">
    <h3>Morgan Ellis, <small>MHA, MBA, CHCIO, CPHIMS</small></h3>
    <p class="role">President and CEO</p>
    <p>As the Founder and CEO of VitaLink HS, Morgan has been working in the technology industry for over 25 years with extensive experience in healthcare and IT. As a consultant Morgan held multiple roles including CIO and CISO. Over the years, Morgan has been the executive sponsor of multiple electronic health record (EHR) implementations... <a href="#">READ MORE</a> <span style="color:var(--purple)">»</span></p>
  </div>
  <svg class="abs" style="left:1148px;top:282px" width="14" height="24" viewBox="0 0 14 24" fill="none" stroke="#6c4a9f" stroke-width="2.5"><path d="M2 2l10 10L2 22"/></svg>
</section>

<section class="contact">
  <h2 class="abs heading">CONTACT US</h2>
  <svg class="abs" style="left:400px;top:140px" width="400" height="20"><line x1="0" y1="10" x2="400" y2="10" stroke="#fff" stroke-width="1.5"/><circle cx="6" cy="10" r="5" fill="#6c4a9f" stroke="#fff" stroke-width="1.5"/><circle cx="394" cy="10" r="5" fill="#6c4a9f" stroke="#fff" stroke-width="1.5"/></svg>
  <div class="abs channel" style="left:139px;top:122px">
    <svg width="58" height="58" viewBox="0 0 58 58"><circle cx="29" cy="29" r="27" fill="none" stroke="#fff" stroke-width="2"/><path d="M22 19c2-1 4 3 5 5s-2 3-1 5 3 4 5 5 3-2 5-1 5 3 4 5c-1 3-5 4-9 2s-9-7-11-11-1-8 2-10z" fill="#fff"/></svg>
    <p style="margin-top:14px">555-010-2682</p>
  </div>
  <div class="abs channel" style="left:438px;top:122px">
    <svg width="58" height="58" viewBox="0 0 58 58"><circle cx="29" cy="29" r="27" fill="var(--purple)" stroke="#fff" stroke-width="2"/><path d="M29 17a8 8 0 0 0-8 8c0 6 8 15 8 15s8-9 8-15a8 8 0 0 0-8-8z" fill="#fff"/><circle cx="29" cy="25" r="3" fill="var(--purple)"/></svg>
    <p style="margin-top:14px">Lorem Ipsum is simply dummy text of the<br>printing.</p>
  </div>
  <div class="abs channel" style="left:741px;top:122px">
    <svg width="58" height="58" viewBox="0 0 58 58"><circle cx="29" cy="29" r="27" fill="none" stroke="#fff" stroke-width="2"/><rect x="18" y="21" width="22" height="16" fill="#fff"/><path d="M18 22l11 8 11-8" fill="none" stroke="var(--purple)" stroke-width="1.5"/></svg>
    <p style="margin-top:14px">mellis@vitalinkhs.example</p>
  </div>
  <div class="abs field" style="left:228px;top:301px;width:365px;height:43px">Name</div>
  <div class="abs field" style="left:228px;top:351px;width:365px;height:42px">Email</div>
  <div class="abs field" style="left:228px;top:405px;width:365px;height:41px">Phone</div>
  <div class="abs field message" style="left:614px;top:301px;width:363px;height:92px">Message</div>
  <div class="abs submit" style="left:614px;top:405px;width:363px;height:41px">SUBMIT</div>
</section>

<footer>2018 ©VitaLink - All Rights Reserved</footer>

</body>
</html>
```